Business Card Design for Consulting Company

I require a Business Card design for my Consulting company. <br/><br/>My company name is: Marek Olvani Consulting Inc.<br/>My website is: www.marekolvaniconsulting.example<br/><br/>My company focuses on management and software development for the Tallobrix CRM platform (www.tallobrix.example)<br/><br/>I have a logo already designed...see attached.
Updates

Also Include my Name and Title: Marek T.L. Olvani President

Target Market(s)

Tallobrix Customers

Contact Information for Business Card

Only include my LOGO (provided)
My Name: Marek TL Olvani
My Title: President
My Company Name: Marek Olvani Consulting Inc.
My Website: www.marekolvaniconsulting.example
My Email: marek.olvani.consulting@mailbox.example

NO PHONE NUMBER
NO ADDRESS

Font styles to use
Serif
Sans Serif
Other font styles liked:
• see my website: www.marekolvaniconsulting.example

Colors

Designer to choose colors to be used in the design.

Requirements
Must have
• Must include my Orange
• Include my name (Marek T.L. Olvani), title (President) company name, website and email
• It should also have a tag line like: Tallobrix Consulting
• I'm flexible with the tag line
Should not have
• Don't include my phone number or address

```html
<!DOCTYPE html>
<html lang="en">
<head>
<meta charset="utf-8">
<title>Marek Olvani Consulting Inc. — Business Card</title>
<link rel="stylesheet" href="https://fonts.googleapis.com/css2?family=Cinzel:wght@400;500&family=EB+Garamond:wght@400&display=swap">
<style>
  :root {
    --bg-dark: #1c1c1c;
    --bg-mid: #333333;
    --orange: #f7861f;
    --orange-light: #fd9b2b;
    --white: #ffffff;
    --paper-shade: #ececec;
  }
  * { box-sizing: border-box; margin: 0; padding: 0; }
  html, body {
    width: 1200px; height: 1200px; overflow: hidden;
  }
  body {
    background: radial-gradient(ellipse at 50% 45%, var(--bg-mid) 0%, var(--bg-dark) 75%);
    position: relative;
  }
  .card {
    position: absolute;
    left: 250px;
    width: 700px;
    height: 400px;
    border-radius: 28px;
    box-shadow: 0 18px 40px rgba(0,0,0,0.5);
    display: flex;
    align-items: center;
  }
  .card--front {
    top: 160px;
    background: linear-gradient(160deg, var(--orange-light) 0%, var(--orange) 100%);
    justify-content: center;
    gap: 26px;
  }
  .card--back {
    top: 640px;
    background: linear-gradient(180deg, var(--white) 40%, var(--paper-shade) 100%);
    padding-left: 70px;
  }
  .brand-square {
    width: 96px; height: 96px;
    border-radius: 16px;
    border: 5px solid var(--white);
    flex: none;
  }
  .company-name {
    font-family: "Cinzel", serif;
    font-weight: 400;
    color: var(--white);
    font-size: 34px;
    line-height: 1.2;
    letter-spacing: 0.5px;
  }
  .brand-block {
    display: flex; flex-direction: column; align-items: center; gap: 14px;
    width: 170px; flex: none;
  }
  .brand-block .brand-square { border-color: var(--orange); width: 110px; height: 110px; }
  .brand-block .brand-name {
    font-family: "Cinzel", serif;
    color: var(--orange);
    font-size: 18px;
    letter-spacing: 0.5px;
  }
  .divider {
    width: 2px; height: 180px;
    background: var(--orange);
    margin: 0 34px 0 40px;
    flex: none;
  }
  .contact { color: var(--orange); }
  .contact__name {
    font-family: "Cinzel", serif;
    font-size: 33px;
    line-height: 1.1;
  }
  .contact__title {
    font-family: "Cinzel", serif;
    font-size: 22px;
    margin: 4px 0 16px;
  }
  .contact__line {
    display: flex; align-items: center; gap: 10px;
    font-family: "EB Garamond", serif;
    font-size: 17px;
    line-height: 1.6;
  }
  .contact__line svg { width: 16px; height: 16px; flex: none; }
</style>
</head>
<body>
  <section class="card card--front">
    <div class="brand-square"></div>
    <h1 class="company-name">Marek Olvani<br>Consulting Inc.</h1>
  </section>

  <section class="card card--back">
    <div class="brand-block">
      <div class="brand-square"></div>
      <span class="brand-name">Marek Olvani</span>
    </div>
    <div class="divider"></div>
    <div class="contact">
      <h2 class="contact__name">Marek TL Olvani</h2>
      <p class="contact__title">President</p>
      <p class="contact__line">
        <svg viewBox="0 0 16 16" aria-hidden="true"><rect x="1" y="3" width="14" height="10" fill="var(--orange)"/><path d="M1 3 L8 9 L15 3" fill="none" stroke="#fff" stroke-width="1.4"/></svg>
        marek.olvani.consulting@mailbox.example
      </p>
      <p class="contact__line">
        <svg viewBox="0 0 16 16" aria-hidden="true" fill="none" stroke="var(--orange)" stroke-width="1.3"><circle cx="8" cy="8" r="6.5"/><ellipse cx="8" cy="8" rx="3" ry="6.5"/><path d="M1.5 8h13M2.5 4.8h11M2.5 11.2h11"/></svg>
        www.marekolvaniconsulting.example
      </p>
    </div>
  </section>
</body>
</html>
```